Vesit cards for web development company

We need a business card design for our company. The company develops online platforms and conducts marketing consulting. Company logo. The cards must fit in with us (a junior start UP), but they must also be professional enough to impress with investors like banks. We wish you a combination of classic and modern design

Target Market(s)

Business partners and IT and marketing customers

Industry/Entity Type

It Company

Contact Information for Business Card

Folgende Information müssen Drauf.
Name, Position, Telefon Nr., Mobile Nr., E-Mail adresse, Optional sind noch Webadresse und HRB Nummer

Colors

Designer to choose colors to be used in the design.

Requirements
Must have
• The cards have to fit into the logo later and have to be dynamic and serious at the same time

```html
<!DOCTYPE html>
<html lang="en">
<head>
<meta charset="utf-8">
<title>Brightlane Digital – Business Card</title>
<link href="https://fonts.googleapis.com/css2?family=Montserrat:wght@400;600;700&display=swap" rel="stylesheet">
<style>
  :root {
    --brand-blue: #1577c2;
    --brand-grey: #8f9093;
    --paper: #ffffff;
    --ink-grey: #8a8a8a;
    --backdrop: #eceae6;
  }
  * { box-sizing: border-box; margin: 0; padding: 0; }
  html, body { width: 1200px; height: 1000px; overflow: hidden; }
  body {
    background: var(--backdrop);
    font-family: "Montserrat", sans-serif;
    position: relative;
  }
  .card {
    position: absolute;
    left: 270px;
    width: 660px;
    height: 377px;
    background: var(--paper);
    box-shadow: 0 6px 18px rgba(0,0,0,0.14);
    overflow: hidden;
  }
  .card--front { top: 70px; }
  .card--back { top: 530px; }

  /* Front */
  .front-split { position: absolute; inset: 0; width: 100%; height: 100%; }
  .front-badge {
    position: absolute;
    left: 50%; top: 50%;
    width: 300px; height: 220px;
    transform: translate(-50%, -50%);
    background: var(--paper);
    display: flex; flex-direction: column;
    align-items: center; justify-content: center;
    gap: 10px;
  }
  .wordmark {
    display: flex; align-items: center; gap: 8px;
    color: var(--brand-blue);
    font-weight: 700;
    text-transform: uppercase;
    letter-spacing: 0.02em;
  }
  .wordmark__dot {
    border-radius: 50%;
    background: var(--brand-blue);
    flex: none;
  }
  .front-badge .wordmark { font-size: 24px; }
  .front-badge .wordmark__dot { width: 16px; height: 16px; }
  .front-badge__email { font-size: 12px; color: var(--ink-grey); letter-spacing: 0.04em; }

  /* Back */
  .back-identity { position: absolute; left: 40px; top: 0; bottom: 0; width: 330px; }
  .back-identity .wordmark { position: absolute; top: 60px; left: 0; font-size: 22px; }
  .back-identity .wordmark__dot { width: 14px; height: 14px; }
  .person { position: absolute; left: 40px; top: 215px; text-align: right; }
  .person__name { font-size: 34px; font-weight: 700; color: var(--brand-blue); line-height: 1; }
  .person__role { font-size: 15px; color: var(--ink-grey); margin-top: 4px; }

  .contact-panel {
    position: absolute; right: 0; top: 0;
    width: 265px; height: 100%;
    background: var(--brand-blue);
  }
  .contact-panel__notch {
    position: absolute; left: 0; top: 168px;
    width: 28px; height: 38px;
    background: var(--paper);
  }
  .contact-box {
    position: absolute; left: 28px; right: 22px; top: 22px; bottom: 22px;
    background: var(--paper);
    outline: 2px dashed #666;
    outline-offset: -10px;
    display: flex; flex-direction: column;
    align-items: center; justify-content: center;
    gap: 8px;
  }
  .contact-item { display: flex; flex-direction: column; align-items: center; gap: 6px; }
  .contact-item__icon { width: 22px; height: 22px; }
  .contact-item__text { font-size: 13px; color: var(--ink-grey); }
</style>
</head>
<body>

<section class="card card--front" aria-label="Business card front">
  <svg class="front-split" viewBox="0 0 660 377" preserveAspectRatio="none" aria-hidden="true">
    <rect width="660" height="377" fill="var(--brand-blue)"/>
    <polygon points="0,150 660,330 660,377 0,377" fill="var(--paper)"/>
    <polygon points="0,166 660,346 660,377 0,377" fill="var(--brand-grey)"/>
  </svg>
  <div class="front-badge">
    <div class="wordmark"><span class="wordmark__dot"></span>Brightlane Digital</div>
    <div class="front-badge__email">hello@brightlane.io</div>
  </div>
</section>

<section class="card card--back" aria-label="Business card back">
  <div class="back-identity">
    <div class="wordmark"><span class="wordmark__dot"></span>Brightlane Digital</div>
    <div class="person">
      <div class="person__name">R.K HALVORSEN</div>
      <div class="person__role">Senior Developer</div>
    </div>
  </div>

  <div class="contact-panel">
    <div class="contact-panel__notch"></div>
    <div class="contact-box">
      <div class="contact-item">
        <svg class="contact-item__icon" viewBox="0 0 24 24" aria-hidden="true">
          <rect x="7" y="2" width="10" height="20" rx="2" fill="none" stroke="var(--brand-blue)" stroke-width="2"/>
          <circle cx="12" cy="18" r="1.2" fill="var(--brand-blue)"/>
        </svg>
        <span class="contact-item__text">+805 4471203</span>
      </div>
      <div class="contact-item">
        <svg class="contact-item__icon" viewBox="0 0 24 24" aria-hidden="true">
          <rect x="2" y="5" width="20" height="14" fill="var(--brand-blue)"/>
          <polyline points="3,6 12,13 21,6" fill="none" stroke="var(--paper)" stroke-width="2"/>
        </svg>
        <span class="contact-item__text">hello@brightlane.io</span>
      </div>
      <div class="contact-item">
        <svg class="contact-item__icon" viewBox="0 0 24 24" aria-hidden="true">
          <circle cx="12" cy="12" r="10" fill="var(--brand-blue)"/>
          <g fill="none" stroke="var(--paper)" stroke-width="1.2">
            <ellipse cx="12" cy="12" rx="4" ry="10"/>
            <line x1="2" y1="12" x2="22" y2="12"/>
            <line x1="12" y1="2" x2="12" y2="22"/>
          </g>
        </svg>
        <span class="contact-item__text">brightlane.io</span>
      </div>
      <div class="contact-item">
        <svg class="contact-item__icon" viewBox="0 0 24 24" aria-hidden="true">
          <rect x="2" y="5" width="20" height="14" fill="var(--brand-blue)"/>
          <line x1="6" y1="12" x2="18" y2="12" stroke="var(--paper)" stroke-width="2"/>
        </svg>
        <span class="contact-item__text">5005 7730412</span>
      </div>
    </div>
  </div>
</section>

</body>
</html>
```